Social Media Graphics - Harbor Climb REVISED

Create 6-7 individual social media graphics (square size) to encourage folks to join our online course called:

The Lantern Ledger Plan
How to Launch a Multi-Million Business From Scratch
Sign Up Today!

IMPORTANT: Make the largest and most prominent text on the graphic be: How to Launch a Multi-Million Business From Scratch

For the color scheme of the graphics, let's try a blue color palette; make sure the graphics appeal to both men and women

Make sure each graphic contains 1 of the 3 pics attached (crop pic as needed); and make sure one of the graphics is all TEXT only.

Target Market(s)

men and women looking to start a business

Industry/Entity Type

Entrepreneurship

Colors
0054AA
0677BA
7BADD7
CADEEF
E8F1F8

Requirements
Must have
• All the text and use the 3 pics provided; one graphic can be all text; Simple, modern design that's easy to read

```html
<!DOCTYPE html>
<html lang="en">
<head>
<meta charset="utf-8">
<title>The Lantern Ledger Plan – Sign Up</title>
<link rel="stylesheet" href="https://fonts.googleapis.com/css2?family=Saira+Condensed:wght@700;800&display=swap">
<style>
  :root {
    --blue-deep: #0054AA;
    --blue-mid: #0677BA;
    --blue-soft: #7BADD7;
    --blue-pale: #CADEEF;
    --blue-mist: #E8F1F8;
    --white: #FFFFFF;
  }
  * { margin: 0; padding: 0; box-sizing: border-box; }
  html, body {
    width: 1200px;
    height: 1200px;
    overflow: hidden;
    background: var(--blue-soft);
  }
  .graphic {
    position: relative;
    width: 1200px;
    height: 1200px;
    background: var(--blue-soft);
    font-family: "Saira Condensed", "Arial Narrow", sans-serif;
  }
  .panel {
    position: absolute;
    left: 37px;
    top: 37px;
    width: 1126px;
    height: 1126px;
    background: linear-gradient(160deg, #0562B0 0%, var(--blue-deep) 100%);
  }
  .course-name {
    position: absolute;
    left: 0;
    right: 0;
    top: 200px;
    text-align: center;
    color: var(--white);
    font-weight: 800;
    font-size: 104px;
    line-height: 1;
    letter-spacing: 4px;
    text-transform: uppercase;
  }
  .headline {
    position: absolute;
    left: 0;
    right: 0;
    top: 592px;
    text-align: center;
    font-weight: 800;
    text-transform: uppercase;
    font-size: 98px;
    line-height: 118px;
    letter-spacing: 2px;
  }
  .headline-line { display: block; color: var(--blue-pale); }
  .headline-line--accent { color: var(--blue-soft); }
  .side-bar {
    position: absolute;
    top: 727px;
    height: 42px;
    background: var(--blue-soft);
  }
  .side-bar--left { left: 37px; width: 64px; }
  .side-bar--right { right: 37px; width: 64px; }
  .cta {
    position: absolute;
    left: 416px;
    top: 960px;
    width: 371px;
    height: 92px;
    background: var(--blue-mist);
    color: var(--blue-deep);
    font-weight: 800;
    font-size: 42px;
    letter-spacing: 1px;
    text-transform: uppercase;
    display: flex;
    align-items: center;
    justify-content: center;
  }
</style>
</head>
<body>
  <main class="graphic">
    <div class="panel"></div>
    <h1 class="course-name">The Lantern<br>Ledger Plan</h1>
    <span class="side-bar side-bar--left"></span>
    <span class="side-bar side-bar--right"></span>
    <h2 class="headline">
      <span class="headline-line">How to launch a</span>
      <span class="headline-line headline-line--accent">Multi-Million Business</span>
      <span class="headline-line">From Scratch</span>
    </h2>
    <div class="cta">Sign up today!</div>
  </main>
</body>
</html>
```